Wealth Education Business Needs Sharp Business Card Design

We need a business card design for a recently launched investor education business called Harbor Crest.

The final design should promote security, empowerment, self improvement and financial gain. The card will ideally promote the stature of the business.

For more information and colours please visit harborcrest.com.au

Target Market(s)

Corporate executives and high net worth individuals

Industry/Entity Type

Education

Contact Information for Business Card

Name
Position
Contact Address
Phone
Mobile
Email
Website

```html
<!DOCTYPE html>
<html lang="en">
<head>
<meta charset="utf-8">
<title>Harbor Crest – Business Card</title>
<link href="https://fonts.googleapis.com/css2?family=Oswald:wght@500;600&family=PT+Sans:wght@400;700&display=swap" rel="stylesheet">
<style>
  :root {
    --navy: #1d2b3f;
    --teal: #1b8d92;
    --grey-name: #8c8f93;
    --ink: #1f2327;
    --paper: #ffffff;
    --backdrop: #e9eaec;
    --rule: #2b3a52;
  }
  html, body {
    margin: 0;
    padding: 0;
    width: 1200px;
    height: 900px;
    overflow: hidden;
    background: var(--backdrop);
  }
  .canvas {
    position: relative;
    width: 1200px;
    height: 900px;
  }
  .card {
    position: absolute;
    top: 160px;
    width: 330px;
    height: 580px;
    border-radius: 22px;
    overflow: hidden;
    box-shadow: 0 10px 30px rgba(0,0,0,0.18);
  }
  .card-front { left: 230px; background: var(--paper); }
  .card-back  { left: 640px; background: var(--navy); }

  .front-band {
    position: relative;
    height: 255px;
    background: var(--navy);
    display: flex;
    align-items: center;
    justify-content: center;
  }
  .front-band::after {
    content: "";
    position: absolute;
    left: 50%;
    bottom: -13px;
    transform: translateX(-50%);
    border-left: 13px solid transparent;
    border-right: 13px solid transparent;
    border-top: 14px solid var(--navy);
  }
  .brand {
    display: flex;
    align-items: center;
    gap: 12px;
  }
  .brand-mark {
    width: 26px;
    height: 26px;
    background: var(--teal);
  }
  .brand-name {
    font-family: "Oswald", sans-serif;
    font-weight: 500;
    font-size: 30px;
    letter-spacing: 2px;
    color: var(--paper);
    text-transform: uppercase;
  }

  .front-details {
    padding-top: 38px;
    text-align: center;
    font-family: "PT Sans", sans-serif;
    color: var(--ink);
  }
  .person-name {
    font-family: "Oswald", sans-serif;
    font-weight: 600;
    font-size: 30px;
    line-height: 1;
    margin: 0;
    text-transform: uppercase;
  }
  .person-name .first { color: var(--teal); }
  .person-name .last { color: var(--grey-name); }
  .person-position {
    font-size: 14px;
    font-weight: 700;
    margin: 4px 0 22px;
  }
  .contact {
    font-size: 15px;
    line-height: 1.3;
    margin: 0 0 16px;
  }
  .web-block {
    margin-top: 6px;
  }
  .rule {
    display: block;
    margin: 0 auto;
  }
  .website {
    font-size: 16px;
    margin: 8px 0;
    letter-spacing: 0.3px;
  }

  .back-brand {
    position: absolute;
    top: 50%;
    left: 0;
    right: 0;
    transform: translateY(-60%);
    display: flex;
    flex-direction: column;
    align-items: center;
    gap: 4px;
  }
  .back-brand .brand-name { font-size: 26px; }
  .back-brand .brand-mark { width: 22px; height: 22px; }
  .tagline {
    font-family: "Oswald", sans-serif;
    font-weight: 500;
    font-size: 10px;
    letter-spacing: 3px;
    color: var(--teal);
    text-transform: uppercase;
    margin-left: 34px;
  }
</style>
</head>
<body>
<div class="canvas">

  <section class="card card-front" aria-label="Business card front">
    <header class="front-band">
      <div class="brand">
        <span class="brand-mark" aria-hidden="true"></span>
        <span class="brand-name">Harbor Crest</span>
      </div>
    </header>
    <div class="front-details">
      <h1 class="person-name"><span class="first">Your</span> <span class="last">Name</span></h1>
      <p class="person-position">Position</p>
      <p class="contact">Suite 8, 42 Quayside Lane<br>Kestrel Bay NSW 2199</p>
      <p class="contact">Tel: 1300 555 014<br>Mob: +612 5550 2741</p>
      <p class="contact">Email: support@harborcrest.com.au</p>
      <div class="web-block">
        <svg class="rule" width="230" height="6" viewBox="0 0 230 6" aria-hidden="true">
          <path d="M0 3 Q115 0 230 3 Q115 6 0 3Z" fill="var(--rule)"/>
        </svg>
        <p class="website">www.harborcrest.com.au</p>
        <svg class="rule" width="230" height="6" viewBox="0 0 230 6" aria-hidden="true">
          <path d="M0 3 Q115 0 230 3 Q115 6 0 3Z" fill="var(--rule)"/>
        </svg>
      </div>
    </div>
  </section>

  <section class="card card-back" aria-label="Business card back">
    <div class="back-brand">
      <div class="brand">
        <span class="brand-mark" aria-hidden="true"></span>
        <span class="brand-name">Harbor Crest</span>
      </div>
      <span class="tagline">Study Build Thrive</span>
    </div>
  </section>

</div>
</body>
</html>
```